Very Simple/Minimal Business Card Design Project

The company operates in the industrial maritime infrastructure sector in Brazil. You can find more information on our website www.navelquor.com.br WE NEED TO LOOK POWERFUL AND SERIOUS
I have attached a copy of the old cards. We would like something more professional / industrial / sexy that also includes the position.

The card can be double sided or not. We would like you to propose as many options.

Thank you
Updates

Many thanks, do let me know if you have any questions. I am under a lot of time pressure to try and have them printed over the next days or so.

Please could you use the following information

for the address: Rua Tapiraçu, 418 - Centro, Rio de Janeiro, 20135-070, Brasil

for the mobile: +55 21 8372 9041
for the landline: +55 21 4067 3859

and position:  Diretor Geral

Thakn you

Target Market(s)

Shipowners, bankers, industrial companies

Industry/Entity Type

Industrial

Requirements
Must have
• POWERFUL
SERIOUS
SOLID
BIG CORPORATION

```html
<!DOCTYPE html>
<html lang="pt-BR">
<head>
<meta charset="utf-8">
<title>Navelquor – Cartão de Visita</title>
<link rel="stylesheet" href="https://fonts.googleapis.com/css2?family=Roboto+Condensed:wght@400;700&display=swap">
<style>
  :root {
    --navy: #272f78;
    --deep-blue: #0a4f94;
    --sea-green: #4a9373;
    --accent-blue: #0a78c0;
    --name-green: #4a9a80;
    --ink: #2a2a2a;
    --frame: #555555;
    --paper: #ffffff;
  }
  html, body {
    margin: 0;
    padding: 0;
    width: 1200px;
    height: 1000px;
    overflow: hidden;
    background: var(--paper);
  }
  .canvas {
    position: relative;
    width: 1200px;
    height: 1000px;
    font-family: "Roboto Condensed", "Arial Narrow", sans-serif;
    color: var(--ink);
  }
  .card-front {
    position: absolute;
    left: 0; top: 0;
    width: 610px; height: 1000px;
  }
  .front-panel {
    position: absolute;
    left: 0; top: 0;
  }
  .brand {
    position: absolute;
    left: 18px;
    top: 446px;
    display: flex;
    align-items: center;
    gap: 8px;
  }
  .brand-square {
    width: 40px;
    height: 40px;
    background: var(--navy);
  }
  .brand-name {
    font-weight: 700;
    font-size: 37px;
    letter-spacing: 0;
    color: var(--navy);
    line-height: 1;
  }
  .address {
    position: absolute;
    left: 450px;
    top: 48px;
    font-size: 21px;
    line-height: 38px;
    letter-spacing: -0.3px;
  }
  .holder {
    position: absolute;
    left: 340px;
    top: 464px;
  }
  .holder-name {
    margin: 0;
    font-size: 36px;
    line-height: 42px;
    font-weight: 400;
    color: var(--name-green);
    letter-spacing: -0.3px;
  }
  .holder-position {
    margin: 4px 0 0;
    font-size: 20px;
    line-height: 24px;
    font-weight: 400;
    color: var(--ink);
  }
  .contacts {
    position: absolute;
    left: 413px;
    top: 788px;
    font-size: 21px;
    line-height: 40px;
    letter-spacing: -0.3px;
  }
  .card-back {
    position: absolute;
    left: 616px;
    top: 3px;
    width: 580px;
    height: 993px;
    box-sizing: border-box;
    border: 1px solid var(--frame);
    display: flex;
    align-items: center;
    justify-content: center;
  }
  .back-brand {
    font-weight: 700;
    font-size: 96px;
    color: var(--navy);
    letter-spacing: 1px;
  }
</style>
</head>
<body>
<div class="canvas">
  <section class="card-front">
    <svg class="front-panel" width="310" height="1000" viewBox="0 0 310 1000" aria-hidden="true">
      <defs>
        <linearGradient id="panelFade" gradientUnits="userSpaceOnUse" x1="0" y1="0" x2="300" y2="0">
          <stop offset="0" stop-color="#0a4f94"/>
          <stop offset="0.6" stop-color="#3f8372"/>
          <stop offset="0.78" stop-color="#4e9470"/>
          <stop offset="1" stop-color="#f4f4f4"/>
        </linearGradient>
      </defs>
      <path d="M0 0 H232 Q364 500 232 1000 H0 Z" fill="url(#panelFade)"/>
      <path d="M232 0 Q364 500 232 1000" fill="none" stroke="var(--accent-blue)" stroke-width="8"/>
    </svg>

    <div class="brand">
      <span class="brand-square"></span>
      <span class="brand-name">NAVELQUOR</span>
    </div>

    <div class="address">
      Rua Tapiraçu, 418<br>
      Centro<br>
      CEP 20135-070<br>
      Rio de Janeiro
    </div>

    <div class="holder">
      <h1 class="holder-name">Rafael Moreno</h1>
      <p class="holder-position">Diretor Geral</p>
    </div>

    <div class="contacts">
      T: + 55 21 4067 3859<br>
      M: + 55 21 8372 9041<br>
      rafael@navelquor.com.br<br>
      www.navelquor.com.br
    </div>
  </section>

  <section class="card-back">
    <span class="back-brand">NAVELQUOR</span>
  </section>
</div>
</body>
</html>
```